BrightPlacely.com Wordpress Theme

Hi,

I am looking for a new theme for my wordpress site. The site looks average at the moment and needs a boost. I want to have a better user experience for publishers and advertisers and the proposition for each needs to be clear with better links to registration for both.

Publisher and Advertiser sign up buttons should be on the home page.

I am leaving the brief open save I request that you use green colours on the template.

I want room to be able to add more tabs on the top level if we introduce a blog or other services.

The layout needs to be solid and please work with the copy that's already there.

see http://brightplacely.example

I am looking forward to reviewing your ideas and designs.
Updates

The button to carbon neutral cert I am going to want to make smaller and put it in the bottom of the site.

Do not go down the too fluffy green route with windmills and fuzzy clouds. I am looking for something simple, professional but also organic with a bit of zest to it. 

We are not a niche player serving ads to green only site with green only ads. We simply neutralise the effect of online advertising campaigns.

Some decent images in the header on rotation could work I am not sure. I think these would have to be abstract and largely if not totally green in colour.

Target Market(s)

BrightPlacely.com is an online ad network. Our targets are publishers and advertisers. We bring them together through providing ad serving to the network we have built on behalf of our advertisers.

Advertisers are agencys, brands, large companies looking to sell online or create awareness of the brand.

Requirements
Must have
• Please keep the site clean and use green and white
• Call to action to both publishers and advertisers to join (buttons on home page)

```html
<!DOCTYPE html>
<html lang="en">
<head>
<meta charset="utf-8">
<title>BrightPlacely.com – Contextual Advertising Network</title>
<link href="https://fonts.googleapis.com/css2?family=Arimo:wght@400;700&family=Archivo+Narrow:wght@700&display=swap" rel="stylesheet">
<style>
  :root {
    --header-green-dark: #4fae2c;
    --header-green-mid: #8fd46a;
    --header-green-light: #c9eeb4;
    --nav-dark: #6b5a00;
    --nav-gold: #ffe300;
    --nav-gold-deep: #f2b400;
    --nav-edge: #e08a00;
    --body-olive: #d8dc8a;
    --body-pale: #eef0bf;
    --side-bg: #eef1dc;
    --band-green: #c7de78;
    --text-dark: #111111;
    --accent-red: #e8303a;
    --cta-green: #3f9a24;
    --cta-green-deep: #2e7a18;
    --cta-text: #ffffff;
  }
  * { box-sizing: border-box; margin: 0; padding: 0; }
  html, body { width: 1200px; height: 900px; overflow: hidden; }
  body {
    position: relative;
    font-family: "Arimo", Arial, sans-serif;
    color: var(--text-dark);
    background: var(--body-olive);
  }

  /* Header */
  .site-header {
    position: absolute; left: 0; top: 0; width: 1200px; height: 212px;
    background:
      radial-gradient(ellipse at 70% 10%, var(--header-green-light) 0%, transparent 55%),
      linear-gradient(180deg, var(--header-green-mid) 0%, var(--header-green-dark) 45%, var(--header-green-mid) 80%, var(--header-green-light) 100%);
  }
  .brand-name {
    position: absolute; left: 38px; top: 52px;
    font-size: 84px; font-weight: 700; letter-spacing: -2px;
    color: #ffffff; line-height: 1;
  }

  /* Navigation */
  .main-nav {
    position: absolute; left: 0; top: 211px; width: 1200px; height: 55px;
    background: var(--nav-dark);
  }
  .nav-tab {
    position: absolute; top: 4px; height: 46px;
    display: flex; align-items: center; justify-content: center;
    background: linear-gradient(180deg, var(--nav-gold-deep) 0%, var(--nav-gold) 30%, var(--nav-gold) 70%, var(--nav-gold-deep) 100%);
    border: 3px solid var(--nav-edge);
    font-family: "Archivo Narrow", "Arial Narrow", sans-serif;
    font-weight: 700; font-size: 16px; color: var(--text-dark);
    text-decoration: none; text-transform: uppercase; white-space: nowrap;
  }
  .nav-tab span {
    background: var(--nav-gold); padding: 2px 5px;
    box-shadow: 0 0 0 2px var(--nav-gold-deep);
  }
  .tab-home { left: 6px; width: 115px; }
  .tab-home span { font-family: "Arimo", Arial, sans-serif; letter-spacing: 4px; font-size: 13px; }
  .tab-advertisers { left: 129px; width: 111px; }
  .tab-publishers { left: 248px; width: 113px; }
  .tab-referrals { left: 370px; width: 108px; }
  .tab-offsetting { left: 490px; width: 112px; }
  .tab-contact { left: 609px; width: 108px; }
  .tab-register {
    left: 729px; width: 471px; font-size: 22px; letter-spacing: 6px;
    font-family: "Arimo", Arial, sans-serif;
  }

  /* Main content */
  .content-area {
    position: absolute; left: 0; top: 266px; width: 746px; height: 634px;
    background: radial-gradient(ellipse at 60% 40%, var(--body-pale) 0%, var(--body-olive) 75%);
  }
  .intro-copy {
    position: absolute; left: 15px; top: 24px; width: 728px;
    font-size: 12.8px; font-weight: 700; line-height: 22.3px; letter-spacing: 1.3px;
    white-space: nowrap;
  }
  .brand-inline { color: var(--accent-red); }
  .feature-list { list-style: none; margin: 22.3px 0; padding-left: 18px; }
  .feature-list li::before { content: "* "; }
  .intro-copy p + p { margin-top: 22.3px; }

  .neutral-badge {
    position: absolute; left: 0; top: 823px; width: 298px; height: 77px;
    background: #ffffff;
  }

  /* Sidebar */
  .sidebar {
    position: absolute; left: 746px; top: 266px; width: 454px; height: 634px;
    background: linear-gradient(180deg, var(--side-bg) 0%, #e6eccd 100%);
  }
  .side-heading {
    position: absolute; left: 0; width: 454px; height: 24px;
    background: linear-gradient(90deg, var(--band-green) 0%, #d9ea9a 55%, var(--band-green) 100%);
    font-size: 27px; font-weight: 700; letter-spacing: 2px; line-height: 22px;
    text-align: center;
  }
  .side-copy {
    position: absolute; left: 16px; top: 45px;
    font-size: 14.5px; font-weight: 700; line-height: 22.3px; letter-spacing: 1.4px;
    white-space: nowrap;
  }
  .side-links {
    position: absolute; list-style: none;
    font-size: 19.5px; font-weight: 700; line-height: 22.3px; letter-spacing: 2px;
    white-space: nowrap;
  }
  .side-links li::before { content: "* "; }
  .side-links a { color: var(--text-dark); text-decoration: none; }
  .side-links .signup-button {
    display: inline-block; padding: 0 10px; border-radius: 4px;
    background: linear-gradient(180deg, var(--cta-green) 0%, var(--cta-green-deep) 100%);
    color: var(--cta-text);
  }
</style>
</head>
<body>
  <header class="site-header">
    <div class="brand-name">BrightPlacely.com</div>
  </header>

  <nav class="main-nav">
    <a class="nav-tab tab-home" href="#"><span>Home</span></a>
    <a class="nav-tab tab-advertisers" href="#"><span>Advertisers</span></a>
    <a class="nav-tab tab-publishers" href="#"><span>Publishers</span></a>
    <a class="nav-tab tab-referrals" href="#"><span>Referrals</span></a>
    <a class="nav-tab tab-offsetting" href="#"><span>Offsetting</span></a>
    <a class="nav-tab tab-contact" href="#"><span>Contact</span></a>
    <a class="nav-tab tab-register" href="#">Register Now</a>
  </nav>

  <main class="content-area">
    <div class="intro-copy">
      <p><span class="brand-inline">BrightPlacely.com</span> is a contextual advertising network and ad exchange that brings<br>
      &nbsp;together publishers<br>
      &nbsp;of high quality content with advertisers, enabling them to reach their target market whils<br>
      t publishers<br>
      monetize their sites through advertising that's in keeping with their sites.</p>
      <ul class="feature-list">
        <li>Hundreds of millions of monthly ad impressions across ours and our partner networks</li>
        <li>170+ content channels to target</li>
        <li>B2B &amp; B2C traffic</li>
        <li>Geo Targeting</li>
        <li>Behavioural Targeting</li>
        <li>Re-Targeting</li>
        <li>Real Time Campaign Tracking &amp; Reporting</li>
        <li>ROI tracking</li>
      </ul>
      <p><span class="brand-inline">BrightPlacely.com</span> collates high quality content across a range of specialist and generalist<br>
      websites and blogs and equips advertisers with the tools to target visitors and optimize campaign<br>
      &nbsp;performance.</p>
      <p>As you may have guested by our name BrightPlacely.com is both responsible and ethical.</p>
      <p>100% of the ads we serve are carbon offset meaning that you can feel good in the fact that the<br>
      &nbsp;environmental impact of your advertising campaign has been neutralized.</p>
    </div>
  </main>

  <div class="neutral-badge" role="img" aria-label="Carbon neutral website certificate badge"></div>

  <aside class="sidebar">
    <h2 class="side-heading" style="top:1px">Advertisers</h2>
    <p class="side-copy"><span class="brand-inline">BrightPlacely.com</span> can provide you access<br>
    to over a billion impressions a month to drive<br>
    quality traffic to your website to convert.<br>
    Our advanced advertising technology enables a<br>
    very high degree of targeting to improve the<br>
    performance of your campaigns.</p>

    <h2 class="side-heading" style="top:217px">Advertisers</h2>
    <ul class="side-links" style="left:51px; top:278px">
      <li><a href="#">Advertiser Information</a></li>
      <li><a href="#">Advertiser Login</a></li>
      <li><a class="signup-button" href="#">Advertiser Sign Up</a></li>
      <li><a href="#">Advertising Formats</a></li>
    </ul>

    <h2 class="side-heading" style="top:430px">Publishers</h2>
    <ul class="side-links" style="left:65px; top:494px">
      <li><a href="#">Advertising Formats</a></li>
      <li><a href="#">Publisher Information</a></li>
      <li><a href="#">Publisher Login</a></li>
      <li><a class="signup-button" href="#">Publisher Sign Up</a></li>
    </ul>
  </aside>
</body>
</html>
```